Honeyvale Stitchery Needs a Beautiful Website

I need a new website for this new E-commerce. I sell handmade baby crochets, e.g. booties, headbands, hats, etc. I need a feminine and soft design to make the moms-to-be say 'oohh ahh'. I'd like pink, blue and gray. I'd like an inviting homepage, and nice regular pages where people can see and order the products.

Industry/Entity Type

Baby

Requirements
Must have
• beautiful, soft, feminine design. Please use pictures of the colors I'd like: brown, yellow, pink and blue. Any combination, but definitely include brown.

```html
<!DOCTYPE html>
<html lang="en">
<head>
<meta charset="utf-8">
<title>Honeyvale Stitchery</title>
<link href="https://fonts.googleapis.com/css2?family=Arimo:wght@400;700&family=Tinos:wght@400;700&family=Fredoka:wght@500;600&display=swap" rel="stylesheet">
<style>
:root{
  --pink:#e84c88;
  --pink-band:#ec5b94;
  --pink-light:#f37e86;
  --blue:#09a9d6;
  --sky:#6cc0d6;
  --slate:#6b82bd;
  --mustard:#e7bf4f;
  --green:#8cbf3f;
  --coral:#f37e7e;
  --text:#4a4a4a;
  --muted:#777;
  --line:#d9d9d9;
  --footer:#ececec;
  --bottom:#e2e2e2;
  --price:#e8647a;
  --title-blue:#1799c6;
}
*{box-sizing:border-box;margin:0;padding:0}
html,body{width:1200px;height:2161px;overflow:hidden}
body{position:relative;background:#fff;font-family:Arimo,Arial,sans-serif;color:var(--text)}
.abs{position:absolute}
.header{position:absolute;left:0;top:0;width:1200px;height:179px;background:linear-gradient(#fff 40%,#eeeeee)}
.brand{left:173px;top:38px;font-family:Tinos,serif;font-size:38px;color:var(--pink);display:flex;align-items:center;gap:12px}
.brand-dot{width:18px;height:18px;border-radius:50%;background:var(--sky)}
.top-links{left:620px;top:41px;font-size:10px;color:#444;display:flex;gap:26px}
.cart{left:864px;top:33px;width:165px;height:29px;border:1px solid #ccc;background:#fff;font-size:10px;display:flex;align-items:center;padding-left:14px;gap:10px}
.search{left:679px;top:82px;width:350px;height:28px;display:flex}
.search-input{flex:1;border:1px solid #ccc;background:#fff;font-size:8px;color:#777;padding:9px 14px}
.search-btn{width:87px;background:#6e6e6e;color:#fff;font-size:9px;display:flex;align-items:center;justify-content:center;gap:6px}
.nav{left:173px;top:131px;width:857px;height:48px;display:flex}
.nav a{flex:1;color:#fff;text-decoration:none;font-size:13px;font-weight:700;padding:18px 0 0 19px}
.hero{left:0;top:179px;width:1200px;height:546px;background:radial-gradient(ellipse at 50% 40%,#f58ab2,var(--pink-band) 70%)}
.slide{left:173px;top:44px;width:857px;height:414px;background:linear-gradient(90deg,#f1eeec,#fafafa 55%,#ededed);box-shadow:0 40px 40px -20px rgba(60,0,20,.6);overflow:hidden}
.slide-photo{left:0;top:0;width:430px;height:414px;background:radial-gradient(ellipse at 45% 55%,#f2b6c9,#e9a6ba 30%,#ede6e2 65%)}
.slide-brand{left:429px;top:82px;font-family:Tinos,serif;font-size:52px;color:var(--pink)}
.slide-h{left:429px;font-family:Fredoka,sans-serif;font-weight:600;color:var(--slate);font-size:38px;line-height:1}
.slide-sub{left:431px;top:277px;font-family:Arimo,sans-serif;font-weight:700;font-size:21px;color:var(--pink)}
.btn{background:var(--pink-light);color:#fff;font-family:Tinos,serif;text-align:center}
.slide-btn{left:429px;top:320px;width:170px;height:42px;line-height:42px;font-size:18px}
.dots{left:556px;top:505px;display:flex;gap:6px}
.dots i{width:11px;height:11px;border-radius:50%;background:#d9d9d9;display:block}
.dots i.on{background:#c8275f}
.welcome{left:0;top:775px;width:1200px;text-align:center;font-family:Tinos,serif;font-size:30px;color:var(--pink)}
.intro{left:220px;top:829px;width:760px;text-align:center;font-size:11.5px;line-height:24px;color:#444}
.tile{top:903px;width:268px;height:124px;display:flex}
.tile-photo{width:137px;height:124px}
.tile-info{flex:1;color:#fff;padding:22px 0 0 22px;font-family:Tinos,serif}
.tile-info p{font-size:15px;line-height:1}
.tile-info h3{font-size:20px;font-weight:400;line-height:1.2}
.tile-btn{margin-top:8px;width:95px;height:26px;border:1px solid #fff;font-size:12px;text-align:center;line-height:24px}
.sec-title{left:173px;top:1068px;font-family:Tinos,serif;font-size:17px;color:var(--pink)}
.select{left:814px;top:1066px;width:215px;height:27px;border:1px solid #bbb;font-size:10px;padding:8px 12px;color:#555}
.select b{position:absolute;right:6px;top:7px;width:12px;height:12px;border:1px solid #999}
.select b:after{content:"";position:absolute;left:3px;top:4px;border:3px solid transparent;border-top-color:#444}
.lead{left:173px;top:1114px;font-size:11.5px;color:#444}
.card{width:195px;height:309px;border:1px solid var(--line);text-align:center}
.card-photo{margin:17px auto 0;width:160px;height:128px}
.card h4{margin-top:16px;font-family:Tinos,serif;font-size:13px;color:var(--title-blue);letter-spacing:.3px}
.card p{margin-top:8px;font-size:10px;line-height:18px;color:#555}
.price{margin-top:6px;font-family:Tinos,serif;font-size:20px;color:var(--price)}
.card .btn{margin:6px auto 0;width:141px;height:31px;line-height:31px;font-size:12px}
.footer{left:0;top:1827px;width:1200px;height:272px;background:var(--footer)}
.fcol{top:1862px}
.fcol h5{font-family:Tinos,serif;font-weight:400;font-size:12px;color:var(--pink);margin-bottom:9px}
.fcol li{list-style:none;font-size:10px;color:#666;line-height:23px}
.news-note{font-size:10px;color:#555;line-height:16px}
.news-input{margin-top:10px;width:220px;height:27px;background:#fff;border:1px solid #ccc;font-size:10px;color:#666;padding:7px 10px}
.news-btn{margin-top:10px;width:220px;height:31px;line-height:31px;font-size:11px}
.bottom{left:0;top:2099px;width:1200px;height:62px;background:var(--bottom)}
.copy{left:173px;top:2124px;font-size:10px;color:#555}
.follow{left:825px;top:2114px;display:flex;align-items:center;gap:10px;font-size:10px;color:#555}
.follow i{display:block;width:28px;height:28px;border-radius:50%;background:#b7b7b7}
</style>
</head>
<body>
<header class="header">
  <div class="abs brand"><span class="brand-dot"></span>Honeyvale Stitchery</div>
  <div class="abs top-links"><span>My Account</span><span>|</span><span>Login</span><span>|</span><span>Register</span></div>
  <div class="abs cart">
    <svg width="14" height="12" viewBox="0 0 14 12"><path d="M0 1h3l2 7h7l2-5H4" fill="none" stroke="#888" stroke-width="1.2"/><circle cx="6" cy="10.5" r="1" fill="#888"/><circle cx="11" cy="10.5" r="1" fill="#888"/></svg>
    <span>Your cart is : 0 Items</span>
  </div>
  <div class="abs search">
    <div class="search-input">ENTER KEYWORD :</div>
    <div class="search-btn"><svg width="10" height="10" viewBox="0 0 10 10"><circle cx="4" cy="4" r="3" fill="none" stroke="#fff" stroke-width="1.4"/><path d="M6 6l3.5 3.5" stroke="#fff" stroke-width="1.4"/></svg>SEARCH</div>
  </div>
  <nav class="abs nav">
    <a style="background:var(--pink)">HOME</a>
    <a style="background:var(--blue)">ABOUT US</a>
    <a style="background:var(--slate)">PRODUCTS</a>
    <a style="background:var(--mustard)">SERVICES</a>
    <a style="background:var(--green)">ONLINE SHOP</a>
    <a style="background:var(--coral)">CONTACT</a>
  </nav>
</header>

<section class="abs hero">
  <div class="abs slide">
    <div class="abs slide-photo" role="img" aria-label="Pink crocheted baby ballet booties with rose trims on a white knit blanket"></div>
    <div class="abs slide-brand">Honeyvale Stitchery</div>
    <div class="abs slide-h" style="top:208px">I SELL HANDMADE</div>
    <div class="abs slide-h" style="top:246px;font-size:34px">BABY CROCHETS</div>
    <div class="abs slide-sub">booties, headbands, hats, etc.</div>
    <div class="abs btn slide-btn">ORDER NOW</div>
  </div>
  <div class="abs dots"><i></i><i></i><i class="on"></i><i></i><i></i></div>
</section>

<h1 class="abs welcome" style="font-weight:400">WELCOME TO HONEYVALE</h1>
<p class="abs intro">Lorem Ipsum is simply dummy text of the printing and typesetting industry. Lorem Ipsum has been the industry's standard dummy text ever since the 1500s, when an unknown printer took a galley of type and scrambled it to make a type specimen book.</p>

<div class="abs tile" style="left:173px">
  <div class="tile-photo" role="img" aria-label="Sleeping baby wearing a blue crocheted crown" style="background:linear-gradient(135deg,#9fc4d2,#e9d7cf 60%,#d9c1b4)"></div>
  <div class="tile-info" style="background:var(--sky)"><p>BABY</p><h3>CROWNS</h3><div class="tile-btn">CLICK HERE</div></div>
</div>
<div class="abs tile" style="left:467px">
  <div class="tile-photo" role="img" aria-label="Pink crocheted ballet booties" style="background:radial-gradient(circle at 50% 65%,#eeb3c4,#eeeae6 70%)"></div>
  <div class="tile-info" style="background:#f48a8f"><p>PINK</p><h3>BALLET</h3><div class="tile-btn">CLICK HERE</div></div>
</div>
<div class="abs tile" style="left:761px">
  <div class="tile-photo" role="img" aria-label="Navy crocheted baby shoe with pink roses" style="background:linear-gradient(135deg,#c9b7ae,#3f4766 55%,#5b6285)"></div>
  <div class="tile-info" style="background:var(--slate)"><p>BABY</p><h3>SHOESX</h3><div class="tile-btn">CLICK HERE</div></div>
</div>

<h2 class="abs sec-title" style="font-weight:400">OUR PRODUCTS</h2>
<div class="abs select">Categories<b></b></div>
<p class="abs lead">Lorem Ipsum is simply dummy text of the printing and typesetting industry. Lorem Ipsum has been the industry's standard dummy text ever since the 1500s...</p>

<div class="abs card" style="left:173px;top:1165px"><div class="card-photo" role="img" aria-label="Turquoise crocheted baby crown" style="background:radial-gradient(ellipse,#6fd3e3,#ececec 70%)"></div><h4>BLUE CROWN</h4><p>Lorem Ipsum is simply dummy<br>text of the printing...</p><div class="price">$ 8.00</div><div class="btn">ORDER NOW</div></div>
<div class="abs card" style="left:393px;top:1165px"><div class="card-photo" role="img" aria-label="Black crocheted baby sneakers" style="background:linear-gradient(160deg,#777,#2b2b2b 50%,#aaa)"></div><h4>BLUE CROWN</h4><p>Lorem Ipsum is simply dummy<br>text of the printing...</p><div class="price">$ 8.00</div><div class="btn">ORDER NOW</div></div>
<div class="abs card" style="left:614px;top:1165px"><div class="card-photo" role="img" aria-label="Navy crocheted baby sneakers with red star" style="background:linear-gradient(160deg,#8d8f95,#34466e 50%,#7f8186)"></div><h4>BLUE CROWN</h4><p>Lorem Ipsum is simply dummy<br>text of the printing...</p><div class="price">$ 8.00</div><div class="btn">ORDER NOW</div></div>
<div class="abs card" style="left:834px;top:1165px"><div class="card-photo" role="img" aria-label="Cream crocheted baby shoes with pink flowers" style="background:linear-gradient(160deg,#cfc6bd,#efe7da 50%,#8d7f72)"></div><h4>BLUE CROWN</h4><p>Lorem Ipsum is simply dummy<br>text of the printing...</p><div class="price">$ 8.00</div><div class="btn">ORDER NOW</div></div>

<div class="abs card" style="left:173px;top:1500px"><div class="card-photo" role="img" aria-label="Brown crocheted baby sneakers with pink star" style="background:linear-gradient(160deg,#7c4e6e,#4b3a33 50%,#e5e1dc)"></div><h4>BLUE CROWN</h4><p>Lorem Ipsum is simply dummy<br>text of the printing...</p><div class="price">$ 8.00</div><div class="btn">ORDER NOW</div></div>
<div class="abs card" style="left:393px;top:1500px"><div class="card-photo" role="img" aria-label="Pink crocheted baby crown" style="background:radial-gradient(ellipse,#e56ccc,#efeaee 70%)"></div><h4>BLUE CROWN</h4><p>Lorem Ipsum is simply dummy<br>text of the printing...</p><div class="price">$ 8.00</div><div class="btn">ORDER NOW</div></div>
<div class="abs card" style="left:614px;top:1500px"><div class="card-photo" role="img" aria-label="Coral crocheted baby shoe with yellow flower" style="background:linear-gradient(160deg,#b8475a,#df6a77 50%,#d9b89a)"></div><h4>BLUE CROWN</h4><p>Lorem Ipsum is simply dummy<br>text of the printing...</p><div class="price">$ 8.00</div><div class="btn">ORDER NOW</div></div>
<div class="abs card" style="left:834px;top:1500px"><div class="card-photo" role="img" aria-label="Mint crocheted baby shoes on tree bark" style="background:linear-gradient(160deg,#5d4a3b,#8fd0cc 50%,#4f3f33)"></div><h4>BLUE CROWN</h4><p>Lorem Ipsum is simply dummy<br>text of the printing...</p><div class="price">$ 8.00</div><div class="btn">ORDER NOW</div></div>

<footer class="abs footer"></footer>
<div class="abs fcol" style="left:174px"><h5>WELCOME</h5><ul><li>Home</li><li>About us</li><li>Product</li><li>Services</li><li>Online Shop</li><li>Contact us</li></ul></div>
<div class="abs fcol" style="left:354px"><h5>INFORMATION</h5><ul><li>Specials</li><li>New products</li><li>Best sellers</li><li>Our stores</li><li>Contact us</li><li>Terms and conditions of use</li><li>About us</li><li>Sitemap</li></ul></div>
<div class="abs fcol" style="left:585px"><h5>MY ACCOUNT</h5><ul><li>My orders</li><li>My favorite products.Login</li><li>Register</li></ul></div>
<div class="abs fcol" style="left:801px"><h5>NEWSLETTER SIGNUP</h5><p class="news-note">Get our recent updates through your email id :</p><div class="news-input">Enter your Email id :</div><div class="btn news-btn">SUBSCRIBE NOW</div></div>

<div class="abs bottom"></div>
<div class="abs copy">Copyright © 2014 Honeyvale.All Rights Reserved</div>
<div class="abs follow"><span>Follow us :</span><i></i><i></i><i></i><i></i></div>
</body>
</html>
```